Pebble

My company name is pebble. The logo is attached. I am the business owner.
Name Gideon Thorpe
Phone number- 5553018826
email- Gideon_thorpe@quillnet.net
Website is not live yet but it will be workwithpebble.com
the current beta link is- https://site.brvhosting.com/pebble-v3/
on the back write “ find creative pros”
Use that beta link as reference for typography and colors on card.

```html
<!DOCTYPE html>
<html lang="en">
<head>
<meta charset="utf-8">
<title>Pebble Business Card</title>
<link rel="stylesheet" href="https://fonts.googleapis.com/css2?family=Montserrat:wght@400;500;700&display=swap">
<style>
  :root {
    --bg: #3a3a3a;
    --card-light: #e6e6e6;
    --card-dark: #1c1c1c;
    --ink-dark: #1a1a1a;
    --ink-light: #f2f2f2;
    --rule: #bdbdbd;
  }
  * { margin: 0; padding: 0; box-sizing: border-box; }
  html, body { width: 1200px; height: 881px; overflow: hidden; }
  body {
    background: var(--bg);
    font-family: "Montserrat", sans-serif;
    position: relative;
  }
  .card {
    position: absolute;
    left: 290px;
    width: 620px;
    height: 354px;
    border-radius: 26px;
  }
  .card-front { top: 50px; background: var(--card-light); color: var(--ink-dark); }
  .card-back { top: 477px; background: var(--card-dark); color: var(--ink-light); }

  .front-wordmark {
    position: absolute;
    top: 118px;
    left: 0; right: 0;
    text-align: center;
    font-weight: 700;
    font-size: 78px;
    letter-spacing: 2px;
  }
  .front-tagline {
    position: absolute;
    top: 262px;
    left: 0; right: 0;
    text-align: center;
    font-weight: 400;
    font-size: 15px;
    letter-spacing: 4px;
  }

  .back-wordmark {
    position: absolute;
    left: 40px;
    top: 146px;
    font-weight: 700;
    font-size: 56px;
    letter-spacing: 1px;
  }
  .back-divider {
    position: absolute;
    left: 318px;
    top: 88px;
    width: 1px;
    height: 178px;
    background: var(--rule);
  }
  .contact {
    position: absolute;
    left: 344px;
    top: 92px;
  }
  .contact-name {
    font-weight: 700;
    font-size: 21px;
    letter-spacing: 1.5px;
  }
  .contact-title {
    font-size: 13px;
    font-weight: 500;
    margin-top: 2px;
    margin-bottom: 16px;
  }
  .contact-list { list-style: none; }
  .contact-item {
    display: flex;
    align-items: center;
    gap: 8px;
    font-size: 14px;
    line-height: 24px;
  }
  .contact-item svg { width: 12px; height: 12px; flex: none; }
</style>
</head>
<body>
  <section class="card card-front">
    <div class="front-wordmark">PEBBLE</div>
    <div class="front-tagline">FIND CREATIVE PROS</div>
  </section>

  <section class="card card-back">
    <div class="back-wordmark">PEBBLE</div>
    <div class="back-divider"></div>
    <div class="contact">
      <div class="contact-name">GIDEON THORPE</div>
      <div class="contact-title">Director</div>
      <ul class="contact-list">
        <li class="contact-item">
          <svg viewBox="0 0 12 12" aria-hidden="true"><path d="M3 1 L5 3.5 L4 5 Q5 7 7 8 L8.5 7 L11 9 L10 11 Q5 11 2.5 8 Q0.5 5 1 2 Z" fill="none" stroke="currentColor" stroke-width="1.1"/></svg>
          <span>5553018826</span>
        </li>
        <li class="contact-item">
          <svg viewBox="0 0 12 12" aria-hidden="true"><rect x="1" y="2.5" width="10" height="7" fill="none" stroke="currentColor" stroke-width="1.1"/><path d="M1 2.5 L6 6.5 L11 2.5" fill="none" stroke="currentColor" stroke-width="1.1"/></svg>
          <span>Gideon_thorpe@quillnet.net</span>
        </li>
        <li class="contact-item">
          <svg viewBox="0 0 12 12" aria-hidden="true"><circle cx="6" cy="6" r="5" fill="none" stroke="currentColor" stroke-width="1.1"/><ellipse cx="6" cy="6" rx="2.2" ry="5" fill="none" stroke="currentColor" stroke-width="0.9"/><path d="M1 6 H11" stroke="currentColor" stroke-width="0.9"/></svg>
          <span>www.workwithpebble.com</span>
        </li>
      </ul>
    </div>
  </section>
</body>
</html>
```